New emerging fitness company

A need a website to advertise my classes & personal training services. I also want a personal touch like showing where I started my own fitness journey.
I need a website where I can upload fitness programs for people to purchase. These will be in various formats like video & written based. I’m looking to have various online fitness programs for purchase either in one lump sum or a subscription. Also in the future products for sale like protein powders & other health products

Target Market(s)

Women aged 18-45, mostly

Industry/Entity Type

Fitness

Coding

Coded - Design and coding required

Number of Pages Required

5+ page

Font styles to use
Sans Serif

Colors
e667a6
e33f95
85acd3
82c8e6

Requirements
Must have
• The ability for people to log in & view exercise plans & programs. Also I’ll be loading these online via video. Must have the ability for clients to pay online. Be easy to use & navigate. Also must link to my logo that I have designed through pixel harbor

```html
<!DOCTYPE html>
<html lang="en">
<head>
<meta charset="utf-8">
<title>Vivid Motion – Fitness</title>
<link rel="stylesheet" href="https://fonts.googleapis.com/css2?family=Montserrat:wght@600;700;800&family=Open+Sans:wght@400;600;700&display=swap">
<style>
:root{
  --pink:#e33f95;
  --pink-soft:#e667a6;
  --ink:#1b1b1d;
  --dark:#141416;
  --grey-bg:#efefef;
  --text:#444;
  --white:#fff;
  --star:#f3a31b;
}
*{box-sizing:border-box;margin:0;padding:0}
html,body{width:1200px;height:3916px;overflow:hidden}
body{position:relative;font-family:"Open Sans",Arial,sans-serif;color:var(--text);background:var(--white)}
.abs{position:absolute}
h2.section-title{font-family:"Montserrat",Arial,sans-serif;font-weight:700;font-size:34px;color:var(--ink);text-align:center;letter-spacing:1px}
.btn{display:inline-flex;align-items:center;gap:10px;background:var(--pink);color:var(--white);font-family:"Montserrat",Arial,sans-serif;font-weight:700;font-size:12px;border-radius:22px;padding:0 6px 0 18px;height:36px;letter-spacing:.5px}
.btn .dot{width:26px;height:26px;border-radius:50%;background:var(--white);display:flex;align-items:center;justify-content:center}
.btn-plain{padding:0 20px}

/* header + hero */
.hero{left:0;top:0;width:1200px;height:640px;background:radial-gradient(ellipse at 62% 45%,#5a5658 0%,#2c2a2c 45%,#121213 100%)}
.nav{left:0;top:0;width:1200px;height:58px;display:flex;align-items:center;padding:0 40px;background:rgba(10,10,12,.75)}
.brand{font-family:"Montserrat",Arial,sans-serif;font-weight:800;font-size:22px;color:var(--pink);display:flex;align-items:center;gap:8px;letter-spacing:1px}
.brand .mark{width:18px;height:18px;background:var(--pink)}
.menu{display:flex;gap:26px;margin-left:auto;margin-right:26px;font-size:11px;font-weight:600;color:#ddd;letter-spacing:.5px}
.menu .active{background:var(--pink);color:#fff;padding:4px 8px;margin:-4px -8px}
.hero-title{left:60px;top:245px;font-family:"Montserrat",Arial,sans-serif;font-weight:800;font-size:40px;color:var(--pink)}
.hero-text{left:60px;top:298px;width:420px;font-size:14px;line-height:20px;color:#eee}
.hero-btn{left:60px;top:360px}

/* programs emblem */
.emblem-frame{left:487px;top:667px;width:226px;height:226px;transform:rotate(45deg);border:10px solid #dcdcdc;background:var(--white)}
.emblem{left:529px;top:620px;width:142px;height:142px;transform:rotate(45deg);background:var(--pink);box-shadow:0 6px 14px rgba(0,0,0,.25)}
.emblem-label{left:500px;top:706px;width:200px;text-align:center;font-family:"Montserrat",Arial,sans-serif;font-weight:800;font-size:17px;color:#fff}
.emblem-dot{left:588px;top:676px;width:24px;height:24px;border-radius:50%;background:#fff}

.programs{left:60px;top:790px;width:1080px;display:flex;justify-content:space-between}
.program{width:250px;display:flex;flex-direction:column;align-items:center;text-align:center}
.program .thumb{width:96px;height:96px;transform:rotate(45deg);margin:14px 0 34px;box-shadow:0 4px 10px rgba(0,0,0,.2)}
.program h3{font-size:14px;font-weight:700;color:var(--ink);margin-bottom:6px}
.program p{font-size:11px;line-height:15px;margin-bottom:16px}
.t1{background:linear-gradient(135deg,#c8b9b2,#8a6e66)}
.t2{background:linear-gradient(135deg,#d9d0c7,#6e6a6c)}
.t3{background:linear-gradient(135deg,#b7c1c9,#55616b)}
.t4{background:linear-gradient(135deg,#ddd,#7b7b80)}

/* journey */
.journey{left:0;top:1135px;width:1200px;height:620px;background:var(--grey-bg)}
.journey h2{left:60px;top:1230px;font-family:"Montserrat",Arial,sans-serif;font-weight:700;font-size:34px;color:var(--ink)}
.journey-text{left:60px;top:1290px;width:540px;font-size:12.5px;line-height:18px}
.journey-text p+p{margin-top:16px}
.journey-btn{left:60px;top:1565px}
.journey-photo{left:770px;top:1180px;width:260px;height:500px;background:linear-gradient(180deg,#e9e6e4 0%,#8c8683 50%,#2d2b2c 100%);border-radius:120px 120px 20px 20px;opacity:.85}
.journey-tri{left:700px;top:1250px}
.corner-tri{left:0;top:1670px}

/* personal training */
.pt-title{left:0;top:1825px;width:1200px}
.pt-cards{left:120px;top:1900px;width:960px;display:flex;gap:30px}
.pt-card{width:300px;background:#fff;box-shadow:0 3px 12px rgba(0,0,0,.15);display:flex;flex-direction:column}
.pt-card .photo{height:200px}
.p1{background:linear-gradient(135deg,#c6b3a4,#5d4e47)}
.p2{background:linear-gradient(135deg,#a8a9ad,#34363b)}
.p3{background:linear-gradient(135deg,#d8cfc8,#7d6d68)}
.pt-card .body{padding:14px 26px 16px;text-align:center}
.pt-card h3{font-size:13px;font-weight:700;color:var(--ink);margin-bottom:6px}
.pt-card p{font-size:11px;line-height:15px}
.pt-card .bar{display:flex;height:36px;font-family:"Montserrat",Arial,sans-serif;font-weight:700;font-size:13px;color:#fff}
.bar .price{flex:1;background:var(--ink);display:flex;align-items:center;justify-content:center}
.bar .more{flex:1;background:var(--pink);display:flex;align-items:center;justify-content:center}

/* products */
.products{left:0;top:2375px;width:1200px;height:560px;background:radial-gradient(ellipse at 50% 60%,#a23a74 0%,#6c1f4c 50%,#3b0f29 100%)}
.prod-title{left:0;top:2440px;width:1200px;color:#fff}
.prod-cards{left:115px;top:2510px;width:970px;display:flex;gap:30px}
.prod{width:220px;height:370px;background:#fff;border-radius:6px;display:flex;flex-direction:column;align-items:center;padding:18px 16px}
.prod .pack{width:130px;height:170px;border-radius:6px;margin-bottom:20px}
.k1{background:linear-gradient(180deg,#e9efe4,#7fae5a)}
.k2{background:linear-gradient(180deg,#3a3a3e,#c43a2c)}
.k3{background:linear-gradient(180deg,#f4eeee,#c7475a)}
.k4{background:linear-gradient(180deg,#2a2a2a,#0d0d0d)}
.stars{display:flex;gap:3px;margin-bottom:8px}
.prod h3{font-size:13px;font-weight:700;color:var(--ink)}
.prod .cost{font-size:12px;margin:6px 0 12px}

/* news */
.news-title{left:0;top:3030px;width:1200px}
.news{top:3110px;width:500px;display:flex;gap:22px}
.news .photo{width:210px;height:320px;flex:none}
.n1{background:linear-gradient(160deg,#d4c6bc,#6a5a52)}
.n2{background:linear-gradient(160deg,#cfcfd2,#4c4a4e)}
.news h3{font-size:14px;font-weight:700;color:var(--ink);margin:10px 0 10px}
.news p{font-size:11.5px;line-height:16px}
.news .more{display:block;margin-top:12px;font-size:10px;font-weight:700;color:var(--pink)}

/* footer */
.footer{left:0;top:3510px;width:1200px;height:370px;background:var(--dark)}
.newsletter{left:150px;top:3540px;width:260px;height:310px;border:1px solid #555;padding:34px 24px;text-align:center;color:#fff}
.newsletter h4{font-family:"Montserrat",Arial,sans-serif;font-size:20px;font-weight:700}
.newsletter .sub{font-size:12px;margin:4px 0 22px;color:#ccc}
.field{height:30px;background:#fff;margin-bottom:12px;font-size:11px;color:#888;text-align:left;padding:7px 10px}
.newsletter .btn{margin-top:10px}
.contact{left:430px;top:3540px;width:300px;color:#fff}
.contact h4{font-family:"Montserrat",Arial,sans-serif;font-size:20px;font-weight:700;margin-bottom:20px}
.c-row{display:flex;gap:14px;margin-bottom:22px}
.c-row .lbl{font-size:10px;color:var(--pink);font-weight:700;letter-spacing:.5px}
.c-row .val{font-size:12px;line-height:17px}
.f-brand{left:800px;top:3560px}
.f-text{left:800px;top:3610px;width:310px;font-size:11.5px;line-height:17px;color:#ddd}
.social{left:800px;top:3740px;display:flex;gap:14px}
.social span{width:30px;height:30px;border-radius:50%;background:var(--pink)}
.foot-tri{left:1120px;top:3800px}
.copy{left:0;top:3880px;width:1200px;height:36px;background:#0a0a0b;font-size:11px;color:var(--pink);text-align:center;line-height:36px}
</style>
</head>
<body>

<!-- header & hero -->
<div class="abs hero" role="img" aria-label="Photo of a woman in sportswear standing in a dark gym"></div>
<header class="abs nav">
  <div class="brand"><span class="mark"></span>VIVID MOTION</div>
  <nav class="menu">
    <span class="active">HOME</span><span>OUR JOURNEY</span><span>PROGRAMS</span><span>PERSONAL TRAINING</span><span>PRODUCTS</span><span>NEWS</span><span>CONTACT US</span>
  </nav>
  <span class="btn">LOGIN <span class="dot"><svg width="10" height="10" viewBox="0 0 10 10"><path d="M3 1l4 4-4 4" stroke="#e33f95" stroke-width="2" fill="none"/></svg></span></span>
</header>
<h1 class="abs hero-title">SHAPE YOUR PERFECT BODY</h1>
<p class="abs hero-text">Lorem Ipsum is simply dummy text of the printing and typesetting industry. Lorem Ipsum has been the industry's standard dummy text ever since.</p>
<span class="abs btn hero-btn">CONTACT US <span class="dot"><svg width="10" height="10" viewBox="0 0 10 10"><path d="M3 1l4 4-4 4" stroke="#e33f95" stroke-width="2" fill="none"/></svg></span></span>

<!-- programs -->
<div class="abs emblem-frame"></div>
<div class="abs emblem"></div>
<div class="abs emblem-dot"></div>
<div class="abs emblem-label">PROGRAMS</div>

<section class="abs programs">
  <div class="program"><div class="thumb t1" role="img" aria-label="Program photo: women training together"></div><h3>Lorem Ipsum is simply</h3><p>Lorem Ipsum is simply dummy text of the printing and typesetting industry lorem ipsum</p><span class="btn btn-plain">PURCHASE NOW</span></div>
  <div class="program"><div class="thumb t2" role="img" aria-label="Program photo: stretching session"></div><h3>Lorem Ipsum is simply</h3><p>Lorem Ipsum is simply dummy text of the printing and typesetting industry lorem ipsum</p><span class="btn btn-plain">PURCHASE NOW</span></div>
  <div class="program"><div class="thumb t3" role="img" aria-label="Program photo: weight workout"></div><h3>Lorem Ipsum is simply</h3><p>Lorem Ipsum is simply dummy text of the printing and typesetting industry lorem ipsum</p><span class="btn btn-plain">PURCHASE NOW</span></div>
  <div class="program"><div class="thumb t4" role="img" aria-label="Program photo: studio class"></div><h3>Lorem Ipsum is simply</h3><p>Lorem Ipsum is simply dummy text of the printing and typesetting industry lorem ipsum</p><span class="btn btn-plain">PURCHASE NOW</span></div>
</section>

<!-- our journey -->
<section class="abs journey"></section>
<h2 class="abs" style="left:60px;top:1230px;font-family:'Montserrat',Arial,sans-serif;font-weight:700;font-size:34px;color:var(--ink)">OUR JOURNEY</h2>
<div class="abs journey-text">
  <p>Lorem Ipsum is simply dummy text of the printing and typesetting industry. Lorem Ipsum has been the industry's standard dummy text ever since the 1500s, when an unknown printer took a galley of type and scrambled it to make a type specimen book. It has survived not only five centuries, but also the leap into electronic typesetting, remaining essentially unchanged. It was popularised in the 1960s with the release of sheets containing passages.</p>
  <p>It is a long established fact that a reader will be distracted by the readable content of a page when looking at its layout. The point of using Lorem Ipsum is that it has a more-or-less normal distribution of letters, as opposed to using content here, making it look like readable English.</p>
</div>
<span class="abs btn journey-btn">LEARN MORE <span class="dot"><svg width="10" height="10" viewBox="0 0 10 10"><path d="M3 1l4 4-4 4" stroke="#e33f95" stroke-width="2" fill="none"/></svg></span></span>
<svg class="abs journey-tri" width="440" height="420" viewBox="0 0 440 420"><polygon points="260,20 420,400 20,330" fill="none" stroke="#e33f95" stroke-width="7"/></svg>
<div class="abs journey-photo" role="img" aria-label="Photo of the founder crouching in workout clothes"></div>
<svg class="abs corner-tri" width="80" height="80" viewBox="0 0 80 80"><polygon points="0,0 70,40 0,80" fill="#e33f95"/></svg>

<!-- personal training -->
<h2 class="abs section-title pt-title">PERSONAL TRAINING</h2>
<section class="abs pt-cards">
  <article class="pt-card"><div class="photo p1" role="img" aria-label="Photo of a trainer coaching a client"></div><div class="body"><h3>Lorem Ipsum is simply</h3><p>Lorem Ipsum is simply dummy text of the printing and typesetting industry lorem ipsum</p></div><div class="bar"><span class="price">$120.00</span><span class="more">VIEW MORE</span></div></article>
  <article class="pt-card"><div class="photo p2" role="img" aria-label="Photo of a one-to-one gym session"></div><div class="body"><h3>Lorem Ipsum is simply</h3><p>Lorem Ipsum is simply dummy text of the printing and typesetting industry lorem ipsum</p></div><div class="bar"><span class="price">$120.00</span><span class="more">VIEW MORE</span></div></article>
  <article class="pt-card"><div class="photo p3" role="img" aria-label="Photo of a dumbbell workout"></div><div class="body"><h3>Lorem Ipsum is simply</h3><p>Lorem Ipsum is simply dummy text of the printing and typesetting industry lorem ipsum</p></div><div class="bar"><span class="price">$120.00</span><span class="more">VIEW MORE</span></div></article>
</section>

<!-- products -->
<section class="abs products" role="img" aria-label="Pink-tinted photo of a gym background"></section>
<h2 class="abs section-title prod-title">OUR PRODUCTS</h2>
<section class="abs prod-cards">
  <div class="prod"><div class="pack k1" role="img" aria-label="Protein shake tub"></div><div class="stars"><svg width="80" height="14" viewBox="0 0 80 14"><g fill="#f3a31b"><path id="s" d="M7 0l2 5h5l-4 3 2 5-5-3-5 3 2-5-4-3h5z"/><use href="#s" x="16"/><use href="#s" x="32"/><use href="#s" x="48"/><use href="#s" x="64"/></g></svg></div><h3>Lorem Ipsum is simply</h3><div class="cost">$120.00</div><span class="btn btn-plain" style="height:30px">Add To Cart</span></div>
  <div class="prod"><div class="pack k2" role="img" aria-label="Whey protein tub"></div><div class="stars"><svg width="80" height="14" viewBox="0 0 80 14"><g fill="#f3a31b"><use href="#s"/><use href="#s" x="16"/><use href="#s" x="32"/><use href="#s" x="48"/><use href="#s" x="64"/></g></svg></div><h3>Lorem Ipsum is simply</h3><div class="cost">$120.00</div><span class="btn btn-plain" style="height:30px">Add To Cart</span></div>
  <div class="prod"><div class="pack k3" role="img" aria-label="Protein powder pouch"></div><div class="stars"><svg width="80" height="14" viewBox="0 0 80 14"><g fill="#f3a31b"><use href="#s"/><use href="#s" x="16"/><use href="#s" x="32"/><use href="#s" x="48"/><use href="#s" x="64"/></g></svg></div><h3>Lorem Ipsum is simply</h3><div class="cost">$120.00</div><span class="btn btn-plain" style="height:30px">Add To Cart</span></div>
  <div class="prod"><div class="pack k4" role="img" aria-label="Black supplement tub"></div><div class="stars"><svg width="80" height="14" viewBox="0 0 80 14"><g fill="#f3a31b"><use href="#s"/><use href="#s" x="16"/><use href="#s" x="32"/><use href="#s" x="48"/><use href="#s" x="64"/></g></svg></div><h3>Lorem Ipsum is simply</h3><div class="cost">$120.00</div><span class="btn btn-plain" style="height:30px">Add To Cart</span></div>
</section>

<!-- news -->
<h2 class="abs section-title news-title">LATEST NEWS</h2>
<article class="abs news" style="left:60px"><div class="photo n1" role="img" aria-label="Photo of women in a group workout"></div><div><h3>Lorem Ipsum is simply</h3><p>It is a long established fact that a reader will be distracted by the readable content of a page when looking at its layout. The point of using Lorem Ipsum is that it has a more-or-less normal distribution of letters, as opposed to using content here, making it look like readable English.</p><span class="more">LEARN MORE ▸</span></div></article>
<article class="abs news" style="left:630px"><div class="photo n2" role="img" aria-label="Photo of a woman lifting a dumbbell"></div><div><h3>Lorem Ipsum is simply</h3><p>It is a long established fact that a reader will be distracted by the readable content of a page when looking at its layout. The point of using Lorem Ipsum is that it has a more-or-less normal distribution of letters, as opposed to using content here, making it look like readable English.</p><span class="more">LEARN MORE ▸</span></div></article>

<!-- footer -->
<footer class="abs footer"></footer>
<div class="abs newsletter">
  <h4>NEWS LETTER</h4>
  <div class="sub">Subscribe To Stay In</div>
  <div class="field">Enter Name</div>
  <div class="field">Enter Email</div>
  <span class="btn">SUBSCRIBE <span class="dot"><svg width="10" height="10" viewBox="0 0 10 10"><path d="M3 1l4 4-4 4" stroke="#e33f95" stroke-width="2" fill="none"/></svg></span></span>
</div>
<div class="abs contact">
  <h4>CONTACT US</h4>
  <div class="c-row"><svg width="16" height="20" viewBox="0 0 16 20"><path d="M8 0a7 7 0 0 0-7 7c0 5 7 13 7 13s7-8 7-13a7 7 0 0 0-7-7z" fill="#e33f95"/><circle cx="8" cy="7" r="2.5" fill="#141416"/></svg><div><div class="lbl">ADDRESS</div><div class="val">Lorem Ipsum is simply dummy text<br>of the printing</div></div></div>
  <div class="c-row"><svg width="16" height="18" viewBox="0 0 16 18"><path d="M3 0h3l1 5-2 1a9 9 0 0 0 5 5l1-2 5 1v3c0 2-1 3-3 3C6 16 0 10 0 3c0-2 1-3 3-3z" fill="#e33f95"/></svg><div><div class="lbl">PHONE</div><div class="val">(55) 555-7840</div></div></div>
  <div class="c-row"><svg width="18" height="14" viewBox="0 0 18 14"><rect width="18" height="14" rx="2" fill="#e33f95"/><path d="M1 2l8 6 8-6" stroke="#141416" stroke-width="1.5" fill="none"/></svg><div><div class="lbl">EMAIL</div><div class="val">hello@vividmotion.com</div></div></div>
</div>
<div class="abs f-brand brand">VIVID MOTION</div>
<p class="abs f-text">Lorem Ipsum is simply dummy text of the printing and typesetting industry. Lorem Ipsum has been the industry's standard dummy text ever since the 1500s, when an unknown printer took a galley of type and scrambled it to make a type specimen book.</p>
<div class="abs social"><span></span><span></span><span></span></div>
<svg class="abs foot-tri" width="80" height="80" viewBox="0 0 80 80"><polygon points="10,0 80,40 10,80" fill="#e33f95"/></svg>
<div class="abs copy">Copyright ©2024 Vivid Motion. All Rights Reserved.</div>

</body>
</html>
```